Awesome ecommerce store banner needed!

We need a sharp, clear, strong banner for one of our subcategory pages on http://www.brixmolt.com
We'd like to incorporate the following image. We'd like the background to be gray or black. We are replacing the Wireless Intercoms banner that is orange (we hate it).
WE do like our other banners, however, so please use them as reference:
SIze: 980 x 380
Two raw images of the intercom we'd like you to encorporate have been included. Choose one or the other depending on what you think would be best. If using the single angle, please duplicate it. We want two intercoms in the banner
Simple and Clean is key:
Text: Wireless Intercoms
Text Color: Can be white/off gray
Text Style: Please keep it clean in line with the website
Background: Black/gray/white

```html
<!DOCTYPE html>
<html lang="en">
<head>
<meta charset="utf-8">
<title>Wireless Intercoms</title>
<link rel="stylesheet" href="https://fonts.googleapis.com/css2?family=Montserrat:wght@800&display=swap">
<style>
  :root {
    --bg-center: #3c3c3c;
    --bg-mid: #272727;
    --bg-edge: #131313;
    --text-white: #ffffff;
    --text-silver: #c4c4c4;
    --product-silver: #a9a9a9;
    --product-grey: #5e5e5e;
    --product-black: #161616;
  }
  html, body {
    margin: 0;
    padding: 0;
    overflow: hidden;
    background: var(--bg-edge);
  }
  .banner {
    position: relative;
    width: 1200px;
    height: 465px;
    overflow: hidden;
    background:
      radial-gradient(ellipse 75% 95% at 58% 0%, var(--bg-center) 0%, var(--bg-mid) 45%, var(--bg-edge) 100%);
    font-family: "Montserrat", "Arial Black", sans-serif;
  }
  .product-photo {
    position: absolute;
    left: 0;
    top: 0;
    width: 610px;
    height: 465px;
  }
  .headline {
    margin: 0;
    font-weight: 800;
  }
  .headline-line,
  .headline-reflection {
    position: absolute;
    margin: 0;
    line-height: 1;
    white-space: nowrap;
    font-weight: 800;
  }
  .headline-line--top {
    top: 58px;
    right: 49px;
    font-size: 116px;
    letter-spacing: 0;
    color: var(--text-white);
  }
  .headline-line--bottom,
  .headline-reflection {
    top: 165px;
    right: 43px;
    font-size: 104px;
    letter-spacing: -6px;
  }
  .headline-line--bottom {
    background: linear-gradient(180deg, var(--text-white) 35%, var(--text-silver) 90%);
    -webkit-background-clip: text;
    background-clip: text;
    color: transparent;
  }
  .headline-reflection {
    color: var(--text-white);
    opacity: 0.2;
    transform: scaleY(-1);
    transform-origin: center 92px;
    -webkit-mask-image: linear-gradient(180deg, rgba(0,0,0,0) 30%, rgba(0,0,0,1) 88%);
    mask-image: linear-gradient(180deg, rgba(0,0,0,0) 30%, rgba(0,0,0,1) 88%);
  }
</style>
</head>
<body>
  <div class="banner">
    <svg class="product-photo" role="img" aria-label="Photo of two silver and black wireless intercom units with antennas, one set behind the other" viewBox="0 0 610 465">
      <defs>
        <linearGradient id="productTone" x1="0" y1="0" x2="1" y2="1">
          <stop offset="0%" stop-color="var(--product-grey)"/>
          <stop offset="40%" stop-color="var(--product-silver)"/>
          <stop offset="75%" stop-color="var(--product-grey)"/>
          <stop offset="100%" stop-color="var(--product-black)"/>
        </linearGradient>
        <radialGradient id="productFade" cx="45%" cy="55%" r="62%">
          <stop offset="0%" stop-color="#fff" stop-opacity="1"/>
          <stop offset="70%" stop-color="#fff" stop-opacity="0.9"/>
          <stop offset="100%" stop-color="#fff" stop-opacity="0"/>
        </radialGradient>
        <mask id="productMask">
          <rect width="610" height="465" fill="url(#productFade)"/>
        </mask>
      </defs>
      <rect x="15" y="0" width="590" height="455" rx="60" fill="url(#productTone)" mask="url(#productMask)"/>
    </svg>

    <h1 class="headline">
      <span class="headline-line headline-line--top">WIRELESS</span>
      <span class="headline-line headline-line--bottom">INTERCOMS</span>
    </h1>
    <p class="headline-reflection" aria-hidden="true">INTERCOMS</p>
  </div>
</body>
</html>
```